Rack card 4"x9" for a construction company

We need to have a design for:
- the holder of rack cards. Letter size
- and the rack cards. Size 4"x9"

I attached a picture of the sample holder for example.

I am putting some of the brochures and pics we have in:

https://files.quillbarrow.net/folders/7Tz4Qm9WpXc2Lr8VbN3kHs6JdYf0aGeUo?usp=sharing

The Bodoni font is on the drive.
The rack card should call to action - to learn about our projects and that we are offering fixed price packages.

One of the sides of the rack card has to show our houses like we show on the website ferncove-builders.ca
Images with short info like on the website http://www.ferncove-builders.ca/our-projects/
Maybe have something like: Learn more about our recent projects at www...

You can use our logo from th pdf files. In the brochure on the cover page we show all the associations we are member of - this is a must to be shown.

Mentioning the website and the phone number is a must.

Bring your ideas.
Don't hesitate to ask questions.

Thanks
Harold

```html
<!DOCTYPE html>
<html lang="en">
<head>
<meta charset="utf-8">
<title>Ferncove Builders – Rack Card</title>
<link href="https://fonts.googleapis.com/css2?family=Bodoni+Moda:wght@500;700&family=Mulish:wght@300;400;600;700&family=Oswald:wght@500&display=swap" rel="stylesheet">
<style>
  :root{
    --navy:#14213d;
    --navy-deep:#0f1a33;
    --olive:#7b7660;
    --olive-light:#a7a28b;
    --paper:#ffffff;
    --mist:#eceded;
    --stage:#e9e6e1;
    --ink:#1d2233;
  }
  *{box-sizing:border-box;margin:0;padding:0}
  html,body{width:1200px;height:1200px;overflow:hidden;background:var(--stage)}
  body{position:relative;font-family:"Mulish",sans-serif;color:var(--ink)}
  .card{position:absolute;left:60px;width:1080px;height:480px;overflow:hidden;box-shadow:0 6px 14px rgba(0,0,0,.25)}
  .card--projects{top:86px;background:var(--paper)}
  .card--dream{top:632px}

  /* shared brand block */
  .brand{position:absolute;text-align:center}
  .brand__mark{display:block;width:58px;height:58px;border-radius:50%;background:var(--olive-light);margin:0 auto 16px}
  .brand__name{font-family:"Bodoni Moda",serif;font-weight:700;color:var(--navy);font-size:34px;line-height:1.05;letter-spacing:1px}

  /* projects card */
  .projects__backdrop{position:absolute;left:275px;top:0;right:0;bottom:0;background:linear-gradient(180deg,#f4f4f4 0%,#e3e4e6 60%,#eeeeee 100%)}
  .projects__brand{left:0;top:0;width:275px;height:226px;background:var(--paper);padding-top:36px}
  .about{position:absolute;left:0;top:226px;width:275px;height:254px;background:var(--navy);color:#fff;padding:14px 28px 0 28px}
  .about__title{font-size:24px;font-weight:400;display:inline-block;border-bottom:1.5px solid #fff;padding-bottom:2px;margin-bottom:14px}
  .about__text{font-size:13.4px;line-height:18.2px;font-weight:300;text-align:justify}
  .projects__headline{position:absolute;left:285px;width:790px;top:20px;text-align:center;font-family:"Bodoni Moda",serif;font-weight:700;color:var(--navy);font-size:35px;line-height:44px;white-space:nowrap}
  .projects__intro{position:absolute;left:300px;width:760px;top:126px;text-align:center;font-size:14.6px;line-height:19.5px;font-weight:400;color:#2a2e3c}
  .house{position:absolute;top:184px;width:176px;background:var(--paper);box-shadow:0 3px 6px rgba(0,0,0,.2)}
  .house__photo{display:block;margin:4px 4px 0;height:140px}
  .house__title{font-family:"Bodoni Moda",serif;font-weight:700;color:var(--olive);font-size:15px;line-height:17px;padding:6px 10px 0;height:48px}
  .house__stats{display:flex;background:var(--olive);color:#fff;height:50px;align-items:center;padding:0 4px}
  .stat{flex:1;text-align:center;border-left:1px solid #fff;line-height:18px}
  .stat:first-child{border-left:none;flex:1.5}
  .stat__label{display:block;font-size:10px;font-weight:600}
  .stat__value{display:block;font-size:14px}
  .contact-bar{position:absolute;right:0;bottom:0;height:40px;width:552px;background:var(--navy);clip-path:polygon(32px 0,100% 0,100% 100%,0 100%);display:flex;align-items:center;justify-content:flex-end;padding-right:18px;gap:10px;color:#fff}
  .contact-bar__url{font-size:19px;font-weight:400}
  .contact-bar__url b{font-weight:700}
  .contact-bar__sep{width:2px;height:28px;background:#fff;margin:0 4px}
  .contact-bar__phone{font-family:"Oswald",sans-serif;font-size:24px;font-weight:500}

  /* dream card */
  .dream__scene{position:absolute;inset:0;background:linear-gradient(90deg,#c9c5c0 0%,#8d8f97 22%,#3c4a68 45%,#1f2c4b 70%,#1b2745 100%)}
  .dream__brand{left:36px;top:0;width:237px;height:236px;background:var(--paper);padding-top:20px;clip-path:polygon(0 0,100% 0,100% 100%,50% 194px,0 100%)}
  .dream__brand::after{content:"";position:absolute;left:0;right:0;bottom:0;height:44px;background:var(--navy);clip-path:polygon(0 100%,50% 0,100% 100%,100% 100%,50% 12px,0 100%)}
  .dream__headline{position:absolute;left:390px;width:670px;top:32px;text-align:center;font-family:"Bodoni Moda",serif;font-weight:700;color:#fff;font-size:48px;line-height:52px;white-space:nowrap}
  .dream__intro{position:absolute;left:425px;width:620px;top:150px;text-align:center;font-size:14.6px;line-height:19.5px;color:#fff}
  .dream__photo{position:absolute;top:228px;width:190px;height:155px;border:3px solid #fff}
  .members{position:absolute;left:0;right:0;bottom:0;height:66px;background:#efefef;display:flex;align-items:center;padding-left:34px}
  .members__label{font-family:"Bodoni Moda",serif;font-weight:700;font-size:20px;color:var(--navy);letter-spacing:.5px;margin-right:26px}
  .badge{width:62px;height:36px;margin-right:24px;border-radius:4px;background:#c7cbd3}
  .badge--round{border-radius:50%;width:52px;height:40px;background:#8fb0c5}
  .badge--red{background:#c9847b;width:48px}
  .badge--green{background:#8db38a;width:40px}
  .badge--navy{background:#6f7fa0;width:52px}
  .badge--blue{background:#3d6fb0;width:88px}
  .members__sep{width:2px;height:40px;background:var(--navy);margin:0 12px 0 4px}
  .members__url{font-size:18px;color:var(--navy);margin-left:10px}
  .members__url b{font-weight:700}
</style>
</head>
<body>

<section class="card card--projects">
  <div class="projects__backdrop" role="img" aria-label="Faint background photo of a house facade"></div>

  <div class="brand projects__brand">
    <span class="brand__mark"></span>
    <div class="brand__name">FERNCOVE<br>BUILDERS</div>
  </div>

  <div class="about">
    <h2 class="about__title">About us</h2>
    <p class="about__text">Ferncove Builders Ltd Founder, Harold Pennick, is a third-generation home builder. Growing up, he was exposed daily to incredible examples of fine construction and craftsmanship. These early lessons ignited a passion for creating masterful single family homes for others</p>
  </div>

  <h1 class="projects__headline">Exquisite, Cost-effective Custom Builds:<br>Your Vision. Your Reality</h1>
  <p class="projects__intro">Here is some of our finest work. Each is an example of a vision we turned to reality using only the highest quality building materials.Tremendous craftsmanship takes work. We're happy to oblige.</p>

  <article class="house" style="left:295px">
    <div class="house__photo" role="img" aria-label="Photo of a dark grey traditional craftsman house" style="background:linear-gradient(180deg,#cfdceb 0%,#5a5f66 45%,#3b4048 75%,#5f8a4a 100%)"></div>
    <h3 class="house__title">Renfrew Traditional Craftsman</h3>
    <div class="house__stats"><div class="stat"><span class="stat__label">BEDROOMS</span><span class="stat__value">7</span></div><div class="stat"><span class="stat__label">BATH</span><span class="stat__value">5</span></div><div class="stat"><span class="stat__label">SQFT</span><span class="stat__value">3828</span></div></div>
  </article>

  <article class="house" style="left:493px">
    <div class="house__photo" role="img" aria-label="Photo of a modern craftsman house with stone facade" style="background:linear-gradient(180deg,#9fb3c6 0%,#5b5a55 40%,#4a4944 75%,#6f8f57 100%)"></div>
    <h3 class="house__title">Burnaby Modern Craftsman</h3>
    <div class="house__stats"><div class="stat"><span class="stat__label">BEDROOMS</span><span class="stat__value">8</span></div><div class="stat"><span class="stat__label">BATH</span><span class="stat__value">8</span></div><div class="stat"><span class="stat__label">SQFT</span><span class="stat__value">7973</span></div></div>
  </article>

  <article class="house" style="left:690px">
    <div class="house__photo" role="img" aria-label="Photo of a lit modern craftsman house at dusk" style="background:linear-gradient(180deg,#1f3f9a 0%,#8c8f96 45%,#c9c7c0 75%,#6f6e69 100%)"></div>
    <h3 class="house__title">Renfrew Modern Craftsman</h3>
    <div class="house__stats"><div class="stat"><span class="stat__label">BEDROOMS</span><span class="stat__value">9</span></div><div class="stat"><span class="stat__label">BATH</span><span class="stat__value">7</span></div><div class="stat"><span class="stat__label">SQFT</span><span class="stat__value">4020</span></div></div>
  </article>

  <article class="house" style="left:888px">
    <div class="house__photo" role="img" aria-label="Photo of a white modern house with front lawn" style="background:linear-gradient(180deg,#2c54b8 0%,#d9d8d2 45%,#eeece6 70%,#6e9a4e 100%)"></div>
    <h3 class="house__title">Kerrisdale Modern Opulence</h3>
    <div class="house__stats"><div class="stat"><span class="stat__label">BEDROOMS</span><span class="stat__value">7</span></div><div class="stat"><span class="stat__label">BATH</span><span class="stat__value">5</span></div><div class="stat"><span class="stat__label">SQFT</span><span class="stat__value">3828</span></div></div>
  </article>

  <div class="contact-bar">
    <svg width="26" height="26" viewBox="0 0 26 26" fill="none" stroke="#fff" stroke-width="1.5"><circle cx="13" cy="13" r="11"/><ellipse cx="13" cy="13" rx="5" ry="11"/><line x1="2" y1="13" x2="24" y2="13"/><line x1="4" y1="8" x2="22" y2="8"/><line x1="4" y1="18" x2="22" y2="18"/></svg>
    <span class="contact-bar__url">www.<b>ferncove-builders</b>.ca</span>
    <span class="contact-bar__sep"></span>
    <svg width="28" height="28" viewBox="0 0 28 28" fill="none" stroke="#fff" stroke-width="1.8"><circle cx="14" cy="14" r="12"/><path d="M9.5 8.5c1-1 2-1 2.5 0l1 2c.3.6 0 1.2-.5 1.5l-.8.5c.6 1.6 1.8 2.8 3.4 3.4l.5-.8c.3-.5.9-.8 1.5-.5l2 1c1 .5 1 1.5 0 2.5-1.5 1.5-4 1-6.5-1.5S8 10 9.5 8.5z" fill="#fff" stroke="none"/></svg>
    <span class="contact-bar__phone">604.555.0187</span>
  </div>
</section>

<section class="card card--dream">
  <div class="dream__scene" role="img" aria-label="Dusk photo of a large modern home beside a neighbouring house"></div>

  <div class="brand dream__brand">
    <span class="brand__mark"></span>
    <div class="brand__name">FERNCOVE<br>BUILDERS</div>
  </div>

  <h1 class="dream__headline">Build The Home Of<br>Your Dreams in Vancouver</h1>
  <p class="dream__intro">Ferncove Builders has a dedicated, experienced staff of professionals standing at the ready to make the vision you have for your dream home a reality. Click the Play Button on the video above to learn more.</p>

  <div class="dream__photo" role="img" aria-label="Photo of a white modern home with a lit entrance" style="left:514px;background:linear-gradient(180deg,#9fb3c6 0%,#e2ded4 45%,#cfcac0 70%,#5f8a45 100%)"></div>
  <div class="dream__photo" role="img" aria-label="Photo of a blue craftsman home behind an iron fence" style="left:737px;background:linear-gradient(180deg,#8fb2d8 0%,#5c7396 45%,#4f6283 70%,#4d7a3a 100%)"></div>

  <div class="members">
    <span class="members__label">PROUD MEMBERS OF</span>
    <span class="badge badge--round"></span>
    <span class="badge badge--red"></span>
    <span class="badge badge--green"></span>
    <span class="badge badge--navy"></span>
    <span class="badge badge--blue"></span>
    <span class="members__sep"></span>
    <svg width="26" height="26" viewBox="0 0 26 26" fill="none" stroke="#14213d" stroke-width="1.5"><circle cx="13" cy="13" r="11"/><ellipse cx="13" cy="13" rx="5" ry="11"/><line x1="2" y1="13" x2="24" y2="13"/><line x1="4" y1="8" x2="22" y2="8"/><line x1="4" y1="18" x2="22" y2="18"/></svg>
    <span class="members__url">www.<b>ferncove-builders</b>.ca</span>
  </div>
</section>

</body>
</html>
```